Become a real French Pastry chef with an easy 3 step pastry kit box.

The company is specialized in French pastries and the boxes will be sold online, and retail stores. The goal is for anyone who likes to be creative and crafty to create and bake their own traditional french pastry in 3 easy steps right at home. French pastries can be known to take hours to bake. These boxes allow you to make them very quickly, no hassle and they results taste amazing. All the ingredients are from FRANCE. Everything you need is in the box, All you need is water! The box design desired is elegant, simple, glamorous but yet eye catchy for retail distribution. This is a kit box with pre scaled ingredients to make your own eclairs. Box dimensions are 8x6x2.
Updates

Target Market(s)

Middle Aged, middle to upper class housewives who enjoy cooking and baking

Industry/Entity Type

Bakery

Font styles to use
Decorative
Script

Colors

Designer to choose colors to be used in the design.

Requirements
Must have
• This box will be called "The eclair kit by {logo}, or {logo} presents the Eclair kit.
• Has to have the instructions (attached document)
• "This box contains: 4 éclair shells, powder pouch, icing bag, pipping bag and pipping tip"
• Net weight 245g
• Nutrition label (attached)
Nice to have
• An eclair on it.

```html
<!DOCTYPE html>
<html lang="en">
<head>
<meta charset="utf-8">
<title>Eclair Kit – Instructions Panel</title>
<link href="https://fonts.googleapis.com/css2?family=Alegreya:wght@400&family=Arimo:wght@400;700&family=Archivo:wght@800&display=swap" rel="stylesheet">
<style>
  :root{
    --backdrop:#d1e6fb;
    --panel:#ffffff;
    --rose:#f2898a;
    --dots:#9a9a9a;
    --ink:#231f20;
    --rule:#bdbdbd;
  }
  *{box-sizing:border-box;margin:0;padding:0}
  html,body{width:1200px;height:1200px;overflow:hidden;background:var(--backdrop)}
  .panel{position:absolute;left:133px;top:256px;width:933px;height:688px;background:var(--panel);box-shadow:6px 6px 4px rgba(0,0,0,.55)}
  .dot-frames{position:absolute;left:0;top:0;width:933px;height:688px}
  .step{position:absolute;left:234px;width:465px;text-align:center;color:var(--rose);font-family:"Alegreya",serif;font-size:16.5px;line-height:23px}
  .step p{white-space:nowrap}
  .step h2{font-weight:400;font-size:24px;line-height:30px;margin-bottom:1px}
  .step-1{top:56px}
  .step-2{top:203px}
  .step-3{top:397px}

  .nutrition{position:absolute;left:21px;top:520px;width:887px;height:146px;border:1px solid var(--ink);font-family:"Arimo",sans-serif;color:var(--ink);font-size:10px}
  .nf-title{position:absolute;left:4px;top:2px;font-family:"Archivo",sans-serif;font-weight:800;font-size:28px;line-height:25px}
  .nf-serving{position:absolute;left:3px;top:55px;line-height:14px}
  .nf-serving b{font-weight:700}
  .nf-col{position:absolute;top:4px;width:246px}
  .nf-col.a{left:164px}
  .nf-col.b{left:415px}
  .nf-head{display:flex;justify-content:space-between;font-size:7.5px;font-weight:700;height:11px;border-bottom:3px solid var(--ink)}
  .nf-row{display:flex;justify-content:space-between;height:15px;line-height:15px;border-bottom:1px solid var(--rule)}
  .nf-row.sub{padding-left:15px}
  .nf-row b{font-weight:700}
  .nf-row:last-child{border-bottom:4px solid var(--ink);height:18px}
  .nf-vit{position:absolute;line-height:12px;white-space:nowrap}
  .nf-bullet{position:absolute;width:4px;height:4px;border-radius:50%;background:var(--ink)}
  .nf-foot{position:absolute;left:663px;top:6px;width:220px;font-size:7px;line-height:9.5px}
  .nf-foot table{border-collapse:collapse;margin-top:2px;width:220px;border-top:1px solid var(--rule)}
  .nf-foot td{padding:0;line-height:9.5px;vertical-align:top}
</style>
</head>
<body>
<div class="panel">
  <svg class="dot-frames" viewBox="0 0 933 688" aria-hidden="true">
    <g fill="none" stroke="var(--dots)" stroke-width="3" stroke-linecap="round" stroke-dasharray="0 17">
      <rect x="234" y="52" width="465" height="106"/>
      <rect x="234" y="200" width="465" height="149"/>
      <rect x="234" y="393" width="465" height="82"/>
    </g>
  </svg>

  <section class="step step-1">
    <h2>Step&nbsp; 1:</h2>
    <p>Mix powder patch with 1 cup of cold water,<br>mix for 2 minutes on high speed. Let the custard<br>rest in fridge for 15 minutes</p>
  </section>
  <section class="step step-2">
    <h2>Step 2:</h2>
    <p>Place pipping tip in pipping bag. Poor custard in bag before<br>cutting the tip off if it off. Pipe custard inside eclair by<br>slightly pressing on flat side of the shell<br>in 3 separate areas for a more uniform filling .<br>Do not over fill or shell will crack</p>
  </section>
  <section class="step step-3">
    <h2>Step 3 :</h2>
    <p>Place&nbsp; icing in warm water for 2 minutes , cut bag at an<br>anglee, then poor on the top of&nbsp; eclair.</p>
  </section>

  <div class="nutrition">
    <div class="nf-title">Nutrition<br>Facts</div>
    <div class="nf-serving">Serving Size 1 éclair (100g)<br>Servings Per Container 4<br><b>Calories</b> 262</div>

    <div class="nf-col a">
      <div class="nf-head"><span>Amount Per Serving</span><span>% Daily Value*</span></div>
      <div class="nf-row"><span><b>Total Fat</b> 16g</span><b>25%</b></div>
      <div class="nf-row sub"><span>Saturated Fat 4.1g</span><b>21%</b></div>
      <div class="nf-row sub"><span>Trans Fat 0g</span><span></span></div>
      <div class="nf-row sub"><span>Polyunsaturated Fat 3.9g</span><span></span></div>
      <div class="nf-row sub"><span>Monounsaturated Fat 6g</span><span></span></div>
      <div class="nf-row"><span><b>Cholesterol</b> 127mg</span><b>42%</b></div>
    </div>
    <div class="nf-col b">
      <div class="nf-head"><span>Amount Per Serving</span><span>% Daily Value*</span></div>
      <div class="nf-row"><span><b>Potassium</b> 3mg</span><b>0%</b></div>
      <div class="nf-row"><span><b>Sodium</b> 337mg</span><b>14%</b></div>
      <div class="nf-row"><span><b>Total Carbohydrate</b> 24g</span><b>8%</b></div>
      <div class="nf-row sub"><span>Dietary Fiber 0.6g</span><b>2%</b></div>
      <div class="nf-row sub"><span>Sugars 7g</span><span></span></div>
      <div class="nf-row"><span><b>Protein</b> 6g</span><b>12%</b></div>
    </div>

    <span class="nf-vit" style="left:164px;top:117px">Vitamin A 16%</span>
    <span class="nf-bullet" style="left:285px;top:120px"></span>
    <span class="nf-vit" style="left:320px;top:117px">Calcium 6%</span>
    <span class="nf-bullet" style="left:412px;top:120px"></span>
    <span class="nf-vit" style="left:456px;top:117px">Iron 6%</span>
    <span class="nf-bullet" style="left:538px;top:120px"></span>
    <span class="nf-vit" style="left:597px;top:117px">Vitamin D 9%</span>
    <span class="nf-vit" style="left:164px;top:131px">Vitamin B6 5%</span>
    <span class="nf-bullet" style="left:285px;top:134px"></span>
    <span class="nf-vit" style="left:311px;top:131px">Vitamin B12 5%</span>
    <span class="nf-bullet" style="left:412px;top:134px"></span>
    <span class="nf-vit" style="left:437px;top:131px">Magnesium 3%</span>

    <div class="nf-foot">
      *Percent Daily Values are based on a 2,000 calorie diet.<br>&nbsp;Your Daily Values may be higher or lower depending on<br>&nbsp;your calorie needs.
      <table>
        <tr><td></td><td>Calories</td><td>2,000</td><td>2,500</td></tr>
        <tr><td>Total Fat</td><td>Less than</td><td>65g</td><td>80g</td></tr>
        <tr><td>&nbsp;Sat Fat</td><td>Less than</td><td>20g</td><td>25g</td></tr>
        <tr><td>Cholesterol</td><td>Less than</td><td>300mg</td><td>300mg</td></tr>
        <tr><td>Sodium</td><td>Less than</td><td>2400mg</td><td>2400mg</td></tr>
        <tr><td>Total Carbs</td><td></td><td>300g</td><td>375g</td></tr>
        <tr><td>&nbsp;Dietary Fiber</td><td></td><td>25g</td><td>30g</td></tr>
      </table>
    </div>
  </div>
</div>
</body>
</html>
```